Letterhead for Dorian Welk

I need a letterhead based on the business card design

Industry/Entity Type

Business

Requirements
Must have
• Footer: Dorian Welk Naturopath
Shop 4123c, 46 Carrow Lane, Sydney 2000

```html
<!DOCTYPE html>
<html lang="en">
<head>
<meta charset="utf-8">
<title>Dorian Welk Naturopath – Letterhead</title>
<link rel="stylesheet" href="https://fonts.googleapis.com/css2?family=Montserrat:wght@500;600;700&family=PT+Sans:wght@400&family=Quicksand:wght@400;500;700&display=swap">
<style>
  :root {
    --orange: #f0953a;
    --ink: #4a4a4a;
    --ink-dark: #2f2f2f;
    --paper: #ffffff;
    --backdrop: #e4e4e4;
    --leaf: #f9e2cd;
  }
  * { box-sizing: border-box; margin: 0; padding: 0; }
  html, body { width: 942px; height: 1200px; overflow: hidden; background: var(--backdrop); }
  .letterhead {
    position: absolute; left: 47px; top: 0;
    width: 848px; height: 1200px;
    background: var(--paper);
    overflow: hidden;
  }
  .brand {
    position: absolute; left: 67px; top: 80px;
    display: flex; align-items: center; gap: 14px;
  }
  .brand-dot { width: 40px; height: 40px; border-radius: 50%; background: var(--orange); }
  .brand-name {
    font-family: "Montserrat", sans-serif; font-weight: 600;
    font-size: 36px; letter-spacing: 1px; color: var(--orange);
  }
  .credentials {
    position: absolute; right: 76px; top: 88px; text-align: right;
    font-family: "Montserrat", sans-serif; color: var(--orange);
  }
  .credentials-title { font-weight: 700; font-size: 17px; line-height: 22px; }
  .credentials-line { font-family: "Quicksand", sans-serif; font-weight: 500; font-size: 13px; line-height: 17px; }
  .meta {
    position: absolute; left: 113px; top: 256px;
    font-family: "Quicksand", sans-serif; font-size: 11px; line-height: 14px; color: var(--ink-dark);
  }
  .meta b { font-weight: 700; }
  .letter-body {
    position: absolute; left: 113px; top: 303px; width: 660px;
    font-family: "PT Sans", sans-serif; font-size: 11.6px; line-height: 24.2px; color: var(--ink);
    text-align: justify;
  }
  .letter-body p { margin-bottom: 24px; }
  .letter-body .salutation { margin-bottom: 0; }
  .signatory {
    position: absolute; left: 113px; top: 728px;
    font-family: "Quicksand", sans-serif; color: var(--ink-dark);
  }
  .signatory-name { font-size: 23px; line-height: 26px; letter-spacing: 0.5px; }
  .signatory-name b { font-weight: 700; }
  .signatory-role { font-size: 12px; line-height: 14px; color: var(--ink); }
  .signature {
    position: absolute; left: 117px; top: 790px; width: 222px; height: 120px;
    background: linear-gradient(135deg, #f7f7f7, #ededed);
  }
  .leaf-decoration {
    position: absolute; left: 0; top: 690px; width: 182px; height: 510px;
    background: linear-gradient(170deg, rgba(249,226,205,0.1), var(--leaf) 55%, rgba(249,226,205,0.6));
    border-radius: 0 60% 55% 0 / 0 45% 50% 0;
  }
  .contact {
    position: absolute; left: 0; top: 1100px; width: 100%; height: 44px;
    font-family: "Quicksand", sans-serif; font-size: 16px; line-height: 21px; color: var(--orange);
  }
  .contact-left { position: absolute; right: 440px; text-align: right; }
  .contact-right { position: absolute; left: 440px; }
  .contact-divider {
    position: absolute; left: 423px; top: 0; width: 1px; height: 42px; background: var(--orange);
  }
  .contact-item { display: flex; align-items: center; gap: 6px; white-space: nowrap; }
  .contact-left .contact-item { justify-content: flex-end; }
  .contact svg { width: 12px; height: 12px; flex: none; }
  .address {
    position: absolute; left: 0; top: 1160px; width: 100%; text-align: center;
    font-family: "Quicksand", sans-serif; font-weight: 500; font-size: 12px; line-height: 16px;
    color: var(--orange); letter-spacing: 0.3px;
  }
  .address b { font-weight: 700; }
</style>
</head>
<body>
  <div class="letterhead">
    <div class="leaf-decoration" role="img" aria-label="Faint large skeleton leaves decoration in soft peach"></div>

    <header>
      <div class="brand">
        <span class="brand-dot"></span>
        <span class="brand-name">DORIAN WELK</span>
      </div>
      <div class="credentials">
        <div class="credentials-title">DORIAN WELK NATUROPATH</div>
        <div class="credentials-line">Bachelor of Health Science</div>
        <div class="credentials-line">Adv. Dip. Naturopathy</div>
      </div>
    </header>

    <div class="meta">
      <div><b>Date :</b> Mon , 25 / 3 / 2013</div>
      <div><b>Recipient :</b> Mr.John Doe Sanderson</div>
    </div>

    <main class="letter-body">
      <p class="salutation">Dear Mr. Jhon Doe</p>
      <p>LoTrem ipsum dolor sit amet, consectetur adipiscing elit. Praesent vulputate, neque ac accumsan suscipit, justo turpis volutpat nisl, tempus fermentum eros tortor et elit. Vivamus porttitor faucibus gravida. Quisque pharetra gravida luctus. Donec eget turpis libero. Ut ac dolor urna, quis tempor nunc. Donec vitae mauris purus, euismod eleifend nulla. Lorem ipsum dolor sit amet, consectetur adipiscing elit. Donec ut purus tellus. Aenean quis dignissim lacus. Vestibulum suscipit vehicula cursus. Suspendisse potenti. Ut in sem nisi. Sed et massa leo.</p>
      <p>Fusce varius libero vel risus condimentum suscipit. Nullam tristique ultrices massa a volutpat. Donec sed dictum metus. Curabitur fringilla nibh eu ligula pharetra a interdum quam aliquam. Maecenas aliquam elit eu orci rutrum molestie. Proin nisl justo, varius a volutpat nec, ultricies sed sem. Nam sit amet imperdiet sem. Phasellus vitae mauris odio. Etiam in purus dui. Etiam ultricies, ante vel iaculis sodales, arcu leo adipiscing leo, sit amet mollis dui nisi non quam.</p>
      <p>Suspendisse sagittis laoreet dolor, vitae rhoncus arcu volutpat quis. Vestibulum at placerat dolor. Vivamus eu lacus ut enim molestie consectetur. Quisque ac lorem vel orci sagittis sollicitudin. Nunc ut quam sem, quis volutpat libero. Cum sociis natoque penatibus et magnis dis parturient montes, nascetur ridiculus mus. Vestibulum ante ipsum primis in faucibus orci luctus et ultrices posuere cubilia Curae; Donec tempor velit in velit feugiat sit amet vulputate nisl posuere..</p>
    </main>

    <div class="signatory">
      <div class="signatory-name"><b>JOHN</b> DOE</div>
      <div class="signatory-role">General director</div>
    </div>
    <div class="signature" role="img" aria-label="Handwritten signature of the signatory"></div>

    <footer>
      <div class="contact">
        <div class="contact-left">
          <div class="contact-item">0400 555 182
            <svg viewBox="0 0 12 12"><rect x="3" y="0.5" width="6" height="11" rx="1.2" fill="none" stroke="currentColor" stroke-width="1.3"/><circle cx="6" cy="9.5" r="0.8" fill="currentColor"/></svg>
          </div>
          <div class="contact-item">dwnaturopath@mailbox.com.au
            <svg viewBox="0 0 12 12"><rect x="0.7" y="2.2" width="10.6" height="7.6" fill="none" stroke="currentColor" stroke-width="1.3"/><path d="M1 2.6 6 6.6 11 2.6" fill="none" stroke="currentColor" stroke-width="1.2"/></svg>
          </div>
        </div>
        <div class="contact-divider"></div>
        <div class="contact-right">
          <div class="contact-item">
            <svg viewBox="0 0 12 12"><circle cx="6" cy="6" r="5.2" fill="none" stroke="currentColor" stroke-width="1.1"/><ellipse cx="6" cy="6" rx="2.3" ry="5.2" fill="none" stroke="currentColor" stroke-width="1"/><path d="M0.8 6h10.4" stroke="currentColor" stroke-width="1"/></svg>
            dorianwelk.com.au
          </div>
          <div class="contact-item">
            <svg viewBox="0 0 12 12"><circle cx="6" cy="6" r="5.2" fill="none" stroke="currentColor" stroke-width="1.1"/><ellipse cx="6" cy="6" rx="2.3" ry="5.2" fill="none" stroke="currentColor" stroke-width="1"/><path d="M0.8 6h10.4" stroke="currentColor" stroke-width="1"/></svg>
            verasolessences.com.au
          </div>
        </div>
      </div>
      <div class="address"><b>Dorian Welk Naturopath</b> · Shop 4123c, 46 Carrow Lane, Sydney 2000</div>
    </footer>
  </div>
</body>
</html>
```